Commercial wall and ceiling contractor needs website

Construction trade companies are notoriously behind the rest of the world when it comes to using current technology to run their businesses; we are not one of those companies. We are a walls and ceilings contractor using up to date communications technologies and applying them unlike any other in our trade. As simple as it sounds, and it really is that simple, it is still a new idea in the trade. We are moving our customers towards communicating with us through a single point of contact using text and email; we distribute information to the appropriate internal party on our end. We need a website that generally appears traditionally familiar to the visitor while also expresses a fresh new approach and edginess to the trade business.

Target Market(s)

General contractors looking to get a bit of background info before inviting us to bid on their projects. This is not a high traffic environment. Their subsequent site visits will be primarily for contact info.

Industry/Entity Type

Construction Company

Number of Pages Required

3 page

Font styles to use
Sans Serif

Requirements
Must have
• The file I uploaded named "kolsite.docx" does not have to appear on the site in the same manner in which appears in the document file; but the info contained within that document does need to be represented on the site.

```html
<!DOCTYPE html>
<html lang="en">
<head>
<meta charset="utf-8">
<title>Veltrac Walls and Ceilings</title>
<link rel="stylesheet" href="https://fonts.googleapis.com/css2?family=Roboto:wght@400;500;700&display=swap">
<style>
  :root {
    --green: #12634a;
    --gold: #b8892c;
    --yellow: #c9ab3a;
    --navy: #0b0b45;
    --brown: #5c4418;
    --teal: #2a6378;
    --ink: #111111;
    --white: #ffffff;
  }
  * { box-sizing: border-box; margin: 0; padding: 0; }
  html, body { width: 1200px; height: 2794px; overflow: hidden; }
  body { position: relative; background: var(--white); font-family: "Roboto", sans-serif; color: var(--ink); }
  .abs { position: absolute; }

  .brand { display: flex; align-items: center; gap: 8px; font-weight: 700; font-size: 15px; letter-spacing: 1px; }
  .brand-mark { width: 24px; height: 24px; border: 3px solid currentColor; }
  .site-header .brand { left: 234px; top: 32px; color: var(--green); }
  .header-rule { left: 0; top: 94px; width: 1200px; height: 1px; background: #e6e6e6; }
  .menu-icon { left: 949px; top: 39px; width: 17px; }
  .menu-icon span { display: block; height: 3px; background: var(--white); margin-bottom: 3px; }

  .btn { display: flex; align-items: center; justify-content: center; background: var(--green); color: var(--white);
         border-radius: 20px; font-weight: 700; font-size: 11.5px; box-shadow: 0 8px 12px rgba(0,0,0,.25); }

  .hero-title { left: 234px; top: 237px; width: 400px; font-size: 22px; font-weight: 700; line-height: 27px; }
  .body-text { font-size: 14.5px; line-height: 18px; }
  .hero-text { left: 234px; top: 341px; width: 375px; }
  .hero-btn { left: 234px; top: 439px; width: 125px; height: 37px; }

  .why-title { left: 514px; top: 880px; font-size: 22px; font-weight: 700; }
  .why-text { left: 514px; top: 933px; width: 445px; }
  .why-btn { left: 514px; top: 1140px; width: 113px; height: 36px; }

  .stat-text-a { left: 234px; top: 1477px; width: 330px; }
  .stat-text-b { left: 609px; top: 1862px; width: 355px; }

  .pie { border-radius: 50%; box-shadow: 0 10px 18px rgba(0,0,0,.25); }
  .pie-hub { border-radius: 50%; background: var(--white); display: flex; align-items: center; justify-content: center; }
  .pie-label { color: var(--white); text-align: center; font-weight: 500; line-height: 1.1; transform: translate(-50%,-50%); }
  .note { font-size: 8.6px; font-weight: 700; text-align: center; line-height: 1.2; transform: translate(-50%,-50%); }

  .contact-title { left: 0; width: 1200px; top: 2180px; text-align: center; font-size: 29px; font-weight: 700; }
  .field { border-bottom: 2px solid var(--gold); font-size: 14.5px; font-weight: 500; padding-bottom: 6px; }
  .field b { color: var(--green); }
  .submit-btn { left: 234px; top: 2413px; width: 125px; height: 37px; font-size: 15px; }
  .info-rule { left: 789px; width: 2px; background: var(--gold); }
  .info-label { left: 801px; color: var(--gold); font-size: 15px; font-weight: 700; }
  .info-value { left: 801px; font-size: 19px; line-height: 23px; }

  .footer .brand { left: 234px; top: 2672px; color: var(--white); font-size: 16px; }
  .footer-head { font-size: 14.5px; font-weight: 700; }
  .footer-links { left: 559px; top: 2680px; font-size: 10.5px; line-height: 14px; }
  .social { left: 888px; top: 2682px; display: flex; gap: 12px; }
  .social span { width: 10px; height: 10px; border-radius: 50%; background: var(--ink); }
  .copyright { right: 234px; top: 2778px; font-size: 8px; }
</style>
</head>
<body>

<header class="site-header">
  <div class="abs brand"><span class="brand-mark"></span>VELTRAC WALLS &amp; CEILINGS</div>
  <div class="abs header-rule"></div>
</header>

<svg class="abs" style="left:0;top:0" width="1200" height="625" aria-hidden="false">
  <defs>
    <linearGradient id="towerTone" x1="0" y1="0" x2="1" y2="1">
      <stop offset="0" stop-color="#d4b23c"/>
      <stop offset="0.55" stop-color="#b08a2c"/>
      <stop offset="1" stop-color="#6b4a1a"/>
    </linearGradient>
  </defs>
  <polygon points="966,0 1200,0 1200,625 590,625" fill="url(#towerTone)" role="img" aria-label="Upward view of glass office towers in a gold tone"/>
  <polygon points="762,0 966,0 868,163" fill="var(--green)"/>
</svg>
<div class="abs menu-icon"><span></span><span></span><span></span></div>

<section class="hero">
  <h1 class="abs hero-title">We are a walls and ceilings contractor using up to date communications technologies</h1>
  <p class="abs body-text hero-text">We are moving our customers towards communicating with us through a single point of contact using text and email; we distribute information to the appropriate internal party on our end.</p>
  <div class="abs btn hero-btn">GET STARTED</div>
</section>

<section class="why">
  <svg class="abs" style="left:0;top:750px" width="537" height="563">
    <defs>
      <radialGradient id="whyTone" cx="0.4" cy="0.4" r="0.8">
        <stop offset="0" stop-color="#cfb44a"/>
        <stop offset="0.7" stop-color="#a5902e"/>
        <stop offset="1" stop-color="#8a6f25"/>
      </radialGradient>
    </defs>
    <polygon points="0,0 537,0 537,91 349,286 537,481 537,563 0,563" fill="url(#whyTone)" role="img" aria-label="Hands holding a phone under business chart graphics with the words Why choose us"/>
  </svg>
  <h2 class="abs why-title">Why Veltrac?</h2>
  <p class="abs body-text why-text">Today’s communication landscape is dramatically different than it was a mere ten years ago.&nbsp; We use our phones less and less for making calls.&nbsp; In fact, it is reported that 70% of direct communication is through text messaging, not phone calls; with text messaging increasing in use by %7,700 since 2008.&nbsp; No surprise here. Think of the phone call process; auto attendant, “…choose 1 for…”, “…if you know the extension…”, “…spell the name…”, “…to hear a directory…”, etc.; ugh.&nbsp; I don’t know about you but when I finally get to the person I want to speak with, I often forget why I called in the first place.&nbsp; And let’s not get started on voicemail; I mean really,</p>
  <div class="abs btn why-btn">LEARN MORE</div>
</section>

<section class="stats">
  <p class="abs body-text stat-text-a">The average length of a phone call has sharply decreased since 2006.&nbsp; That’s because it’s easier to swap a bunch of short messages than it is to interrupt each other’s work at hand with a phone call.&nbsp;&nbsp; Furthermore, 99% of text messages are read while only 33% of voicemail messages are heard; 95% of text messages are read within 3 minutes and, on average, responded to within 90 seconds.</p>

  <div class="abs pie" style="left:696px;top:1468px;width:158px;height:158px;background:conic-gradient(var(--brown) 0 30deg, var(--navy) 30deg 140deg, var(--green) 140deg 250deg, var(--brown) 250deg 360deg)"></div>
  <div class="abs pie-hub" style="left:750px;top:1522px;width:50px;height:50px">
    <svg width="22" height="26" viewBox="0 0 22 26"><rect x="3" y="1" width="14" height="24" rx="2" fill="none" stroke="var(--teal)" stroke-width="2"/><path d="M9 12 l3 3 l7 -7" fill="none" stroke="var(--gold)" stroke-width="2.5"/></svg>
  </div>
  <div class="abs pie-label" style="left:746px;top:1512px;font-size:10.5px">10x<br>Quicker</div>
  <div class="abs pie-label" style="left:825px;top:1546px;font-size:9.5px">90<br>seconds<br>Avarage<br>Response<br>Time</div>
  <div class="abs pie-label" style="left:760px;top:1591px;font-size:10px">5 Seconds</div>

  <div class="abs note" style="left:621px;top:1486px">Texting Is 10x<br>Quicker Than A<br>Phone Call</div>
  <div class="abs note" style="left:630px;top:1611px">On Average, Text<br>Messages Are Read<br>Is Under 5 Seconds</div>
  <div class="abs note" style="left:923px;top:1546px">Average Respponse<br>Time For A Text Is<br>90 Seconds (WCA)</div>

  <svg class="abs" style="left:0;top:0;pointer-events:none" width="1200" height="2794" fill="none" stroke="var(--green)" stroke-width="1.4" stroke-dasharray="2 2">
    <path d="M622 1508 C640 1530 680 1520 705 1495"/><path d="M698 1492 l8 2 l-2 8" stroke-dasharray="none"/>
    <path d="M627 1634 C640 1660 700 1660 730 1628"/><path d="M722 1628 l8 -1 l-1 8" stroke-dasharray="none"/>
    <path d="M925 1530 C970 1500 950 1480 920 1482 C880 1485 900 1505 860 1528"/><path d="M866 1522 l-7 7 l9 2" stroke-dasharray="none"/>
    <path d="M312 1870 C320 1855 345 1855 363 1882"/><path d="M356 1880 l8 3 l0 -8" stroke-dasharray="none"/>
    <path d="M513 1880 C505 1862 480 1865 466 1880"/><path d="M470 1872 l-4 8 l8 1" stroke-dasharray="none"/>
    <path d="M325 2002 C345 2006 355 2000 360 1985"/><path d="M354 1990 l6 -6 l3 8" stroke-dasharray="none"/>
    <path d="M505 2003 C495 2010 480 2008 470 1998"/><path d="M472 2006 l-2 -8 l8 1" stroke-dasharray="none"/>
  </svg>

  <div class="abs pie" style="left:348px;top:1877px;width:136px;height:136px;background:conic-gradient(var(--navy) 0 90deg, var(--green) 90deg 180deg, var(--brown) 180deg 270deg, var(--teal) 270deg 360deg)"></div>
  <div class="abs pie-hub" style="left:395px;top:1924px;width:42px;height:42px">
    <svg width="18" height="22" viewBox="0 0 22 26"><rect x="3" y="1" width="14" height="24" rx="2" fill="none" stroke="var(--teal)" stroke-width="2"/><path d="M9 12 l3 3 l7 -7" fill="none" stroke="var(--gold)" stroke-width="2.5"/></svg>
  </div>
  <div class="abs pie-label" style="left:382px;top:1917px;font-size:10px">33%<br><span style="font-size:6px">Of Adults</span></div>
  <div class="abs pie-label" style="left:448px;top:1912px;font-size:10px">48%<br><span style="font-size:6px">of Business</span></div>
  <div class="abs pie-label" style="left:388px;top:1977px;font-size:10px">78%<br><span style="font-size:6px">Of Consumers</span></div>
  <div class="abs pie-label" style="left:445px;top:1977px;font-size:10px">79%<br><span style="font-size:6px">Of Bosses</span></div>

  <div class="abs note" style="left:284px;top:1893px;font-size:7.6px">33% American adults prefer<br>texts to all other forms of<br>communication (Northfield)</div>
  <div class="abs note" style="left:545px;top:1893px;font-size:7.6px">Only 48% of Business<br>are Equipped to Handle<br>Messaging (Relaymark)</div>
  <div class="abs note" style="left:291px;top:2000px;font-size:7.6px">78% Of Consumers<br>Wish they could<br>text business</div>
  <div class="abs note" style="left:546px;top:1991px;font-size:7.6px">79% of Bosses are<br>Supportive of texting<br>for business purposes</div>

  <p class="abs body-text stat-text-b">One of the many ways that Veltrac is bringing technology to its trade is through communication tools. A single point of contact gets you where you want to go.&nbsp; We distribute the text and email internally.&nbsp; Not only that, we share equal access to our communication points to hold each other accountable for their respective responsibilities.&nbsp; This flow of information is a more efficient, effective, and direct.</p>
</section>

<section class="contact">
  <h2 class="abs contact-title">Get In Touch!</h2>
  <div class="abs field" style="left:234px;top:2240px;width:188px">Enter&nbsp; Name <b>*</b></div>
  <div class="abs field" style="left:441px;top:2240px;width:188px">Enter&nbsp; Email <b>*</b></div>
  <div class="abs field" style="left:234px;top:2287px;width:395px">Enter&nbsp; Subject <b>*</b></div>
  <div class="abs field" style="left:234px;top:2334px;width:395px;height:47px">Message <b>*</b></div>
  <div class="abs btn submit-btn">SUBMIT</div>

  <svg class="abs" style="left:754px;top:2250px" width="24" height="32" viewBox="0 0 24 32"><path d="M4 2 l6 0 l2 8 l-4 3 c2 5 4 8 7 10 l3 -3 l6 3 l-1 7 c-10 0 -20 -12 -19 -28 z" fill="var(--green)"/></svg>
  <div class="abs info-rule" style="top:2247px;height:42px"></div>
  <div class="abs info-label" style="top:2243px">Phone</div>
  <div class="abs info-value" style="top:2265px">604-555-0182</div>

  <svg class="abs" style="left:754px;top:2321px" width="28" height="20" viewBox="0 0 28 20"><rect x="1" y="1" width="26" height="18" fill="none" stroke="var(--green)" stroke-width="2"/><path d="M1 1 l13 10 l13 -10 M1 19 l9 -8 M27 19 l-9 -8" fill="none" stroke="var(--green)" stroke-width="2"/></svg>
  <div class="abs info-rule" style="top:2313px;height:56px"></div>
  <div class="abs info-label" style="top:2309px">Email</div>
  <div class="abs info-value" style="top:2331px">hello@veltracwall<br>sandceilings.com</div>
</section>

<footer class="footer">
  <svg class="abs" style="left:0;top:2576px" width="1200" height="218">
    <polygon points="0,0 341,0 541,218 0,218" fill="var(--gold)"/>
    <polygon points="366,26 398,26 578,218 546,218" fill="var(--green)"/>
  </svg>
  <div class="abs brand"><span class="brand-mark"></span>VELTRAC</div>
  <div class="abs footer-head" style="left:559px;top:2650px">Legal Info</div>
  <div class="abs footer-links">Terms Of Use<br>Privacy Policy<br>Copyright Policy</div>
  <div class="abs footer-head" style="left:888px;top:2650px">Follow Us</div>
  <div class="abs social"><span></span><span></span><span></span><span></span></div>
  <div class="abs copyright">Copyright © 2019 Veltrac</div>
</footer>

</body>
</html>
```